Free Range Egg Farmer wants a Egg Carton Design

We need a design for Free Range Egg carton. Our company name is "BrookHaven The Craft of Growing"

We run a environmentally friendly farm in Gippsland VIC and we produce Free Range Eggs and Pasture Fed Meats in open pasture.

We also run a farm stay business in a very high energy star rating house.
The farm guest participates in our farm activity such as looking after farm animals, maintaining the vegetable garden, cooking fresh food, Yoga and Meditation.

We would like to see designs with our logo and something alternative rather than a typical free range egg cartons.

The team had a meeting and came up with one idea.
"The meditating hen" with thought bubble which we can change the hen's thought by printing batch.
You could either use this idea or create your own.

I have attached 3 photos close to my image as examples.
I also have attached the typical free range egg cartons as examples.

Sticker size is attached. The sticker fits between the case closure system. So there is no need to make spaces for the closure gaps.
Please place Best Before stamp area at the top right corner of the main (middle) section.
Updates

I have post an update to my brief. Please have a look again. BrookHaven

Industry/Entity Type

Printing

Requirements
Must have
• Company name,
Address,
contact number,
facebook logo,
best before date (space to put the stamp on)
12 Free Range Eggs xxx g
Nutrition info

```html
<!DOCTYPE html>
<html lang="en">
<head>
<meta charset="utf-8">
<title>BrookHaven Free Range Eggs – Carton Sticker</title>
<link href="https://fonts.googleapis.com/css2?family=Zilla+Slab:wght@600;700&family=Libre+Baskerville:ital,wght@0,400;0,700;1,400;1,700&family=Open+Sans:wght@400;600;700&display=swap" rel="stylesheet">
<style>
  :root {
    --page: #ececec;
    --cream: #efe6c9;
    --red: #b3393a;
    --forest: #1f4b3b;
    --ink: #2d2a26;
    --grass: #6c9a3e;
    --grass-light: #9cc25a;
    --bubble-line: #74c3d8;
    --bubble-fill: #fbf7ea;
    --hen-gold: #e7a332;
    --hen-brown: #8a3a24;
  }
  * { box-sizing: border-box; margin: 0; padding: 0; }
  html, body { width: 1200px; height: 1200px; overflow: hidden; }
  body { background: var(--page); font-family: "Open Sans", sans-serif; color: var(--ink); }

  .canvas { position: relative; width: 1200px; height: 1200px; }
  .sticker {
    position: absolute; left: 100px; top: 200px; width: 1000px;
    box-shadow: 0 6px 24px rgba(0,0,0,.12);
  }
  .panel { position: relative; width: 1000px; background: var(--cream); overflow: hidden; }
  .panel--back { height: 170px; border-bottom: 1px dashed rgba(0,0,0,.18); }
  .panel--main { height: 430px; }
  .panel--front { height: 180px; border-top: 1px dashed rgba(0,0,0,.18); }

  .art { position: absolute; display: block; }
  .grass { background: linear-gradient(180deg, var(--grass-light), var(--grass)); }
  .hen { background: radial-gradient(ellipse at 55% 55%, var(--hen-gold) 0%, #d98e2c 45%, var(--hen-brown) 80%, rgba(138,58,36,0) 100%); border-radius: 40%; }

  .brand-mark { display: flex; align-items: center; gap: 10px; }
  .brand-mark__dot { width: 72px; height: 72px; border-radius: 50%; background: var(--forest); flex: none; display: block; }
  .brand-name { font-family: "Libre Baskerville", serif; color: var(--forest); }
  .tagline { font-style: italic; display: block; }

  /* back panel */
  .nutrition { position: absolute; left: 220px; top: 28px; width: 480px; font-size: 10.5px; line-height: 1.45; border-left: 2px solid var(--red); padding-left: 12px; }
  .nutrition__title { font-weight: 700; color: var(--red); font-size: 14px; margin-bottom: 2px; }
  .nutrition__strong { font-weight: 700; color: var(--red); }
  .panel--back .brand-mark { position: absolute; right: 40px; top: 30px; flex-direction: column; align-items: flex-end; gap: 6px; }
  .panel--back .brand-mark__dot { width: 60px; height: 60px; }
  .panel--back .brand-name { font-size: 15px; text-align: right; line-height: 1.3; }

  /* main panel */
  .thought {
    position: absolute; left: 290px; top: 22px; width: 560px; height: 112px;
    border: 4px solid var(--bubble-line); border-radius: 56px; background: var(--bubble-fill);
    display: flex; flex-direction: column; justify-content: center; align-items: center;
    font-family: "Libre Baskerville", serif; font-style: italic; font-weight: 700;
    color: var(--forest); font-size: 15.5px; line-height: 1.45; text-align: center;
  }
  .thought__lead { font-size: 19px; }
  .thought-dot { position: absolute; border: 3px solid var(--bubble-line); border-radius: 50%; background: var(--bubble-fill); }
  .best-before { position: absolute; right: 28px; top: 22px; font-weight: 700; font-size: 12px; letter-spacing: .3px; }

  .headline { position: absolute; display: flex; align-items: center; font-family: "Zilla Slab", serif; color: var(--red); text-transform: uppercase; white-space: nowrap; font-weight: 700; }
  .headline__count { line-height: .8; }
  .headline__words { display: flex; flex-direction: column; line-height: 1; margin-left: 16px; }
  .headline__line { display: flex; align-items: flex-end; }
  .headline__weight { font-weight: 600; border-left: 3px solid var(--red); padding-left: 8px; margin-left: 18px; line-height: .9; }

  .panel--main .headline { left: 300px; top: 170px; }
  .panel--main .headline__count { font-size: 168px; }
  .panel--main .headline__words { font-size: 54px; }
  .panel--main .headline__weight { font-size: 40px; }

  .panel--main .brand-block { position: absolute; right: 190px; top: 326px; font-size: 19px; line-height: 1.3; text-align: right; }
  .panel--main .brand-mark__dot { position: absolute; left: 840px; top: 255px; width: 125px; height: 125px; }

  /* front panel */
  .contact { position: absolute; left: 30px; top: 30px; }
  .contact .brand-mark__dot { width: 70px; height: 70px; }
  .contact__text { font-size: 13.5px; line-height: 1.45; }
  .contact__text .brand-name { font-size: 17px; font-weight: 700; }
  .social-square { width: 22px; height: 22px; background: var(--grass); margin: 8px 0 0 80px; }
  .panel--front .headline { right: 60px; top: 44px; }
  .panel--front .headline__count { font-size: 112px; }
  .panel--front .headline__words { font-size: 38px; margin-left: 12px; }
  .panel--front .headline__weight { font-size: 30px; margin-left: 14px; }
</style>
</head>
<body>
<main class="canvas">
  <section class="sticker">

    <div class="panel panel--back">
      <div class="art grass" role="img" aria-label="Grass strip" style="left:0;bottom:0;width:200px;height:22px"></div>
      <div class="art hen" role="img" aria-label="Illustration of a standing hen" style="left:40px;top:22px;width:130px;height:120px"></div>
      <div class="nutrition">
        <p class="nutrition__title">Nutrition Facts</p>
        <p>Serv. size 1egg(44g) • Servings: Calories 70 • Calories from fat 35</p>
        <p>Amount per serving % daily value</p>
        <p><span class="nutrition__strong">Total fat 4g-6%</span> • Saturated fat 1.5g-8% • Trans fat 0g • <span class="nutrition__strong">Cholesterol 190mg-62%</span></p>
        <p class="nutrition__strong">Sodium 55mg-2%</p>
        <p><span class="nutrition__strong">Total Carb. 1g-0% • Protein 6g-10%</span></p>
        <p>Vitamin A 6% • Vitamin C 0% • Calcium 2% • Iron 4%</p>
        <p>Not a significant source of dietary fiber or sugars.</p>
      </div>
      <div class="brand-mark">
        <span class="brand-mark__dot"></span>
        <p class="brand-name">BrookHaven<span class="tagline">The Craft of Growing</span></p>
      </div>
    </div>

    <div class="panel panel--main">
      <div class="art grass" role="img" aria-label="Grass edge along top" style="left:0;top:0;width:1000px;height:18px"></div>
      <div class="art hen" role="img" aria-label="Illustration of a hen thinking, facing right" style="left:10px;top:55px;width:250px;height:320px"></div>
      <div class="art grass" role="img" aria-label="Grass meadow along bottom" style="left:0;bottom:0;width:1000px;height:44px"></div>

      <span class="thought-dot" style="left:262px;top:120px;width:22px;height:18px"></span>
      <span class="thought-dot" style="left:246px;top:142px;width:12px;height:10px"></span>
      <div class="thought">
        <p class="thought__lead">Like this Egg,</p>
        <p>you are full of your own opinions and speculations.</p>
        <p>How can I show you Zen unless you first break your egg?</p>
      </div>
      <p class="best-before">BEST BEFORE DATE</p>

      <h1 class="headline">
        <span class="headline__count">12</span>
        <span class="headline__words">
          <span class="headline__line">Free Range</span>
          <span class="headline__line">Eggs<span class="headline__weight">520g</span></span>
        </span>
      </h1>

      <p class="brand-block brand-name">BrookHaven<span class="tagline">The Craft of Growing</span></p>
      <span class="brand-mark__dot"></span>
    </div>

    <div class="panel panel--front">
      <div class="contact">
        <div class="brand-mark">
          <span class="brand-mark__dot"></span>
          <div class="contact__text">
            <p class="brand-name">BrookHaven - <span style="font-style:italic">The Craft of Growing</span></p>
            <p>Address : Location Street, Location here,<br>here Location.</p>
            <p>Phone : 123 1234 1234</p>
          </div>
        </div>
        <div class="social-square"></div>
      </div>
      <h2 class="headline">
        <span class="headline__count">12</span>
        <span class="headline__words">
          <span class="headline__line">Free Range</span>
          <span class="headline__line">Eggs<span class="headline__weight">520g</span></span>
        </span>
      </h2>
    </div>

  </section>
</main>
</body>
</html>
```